CASH PAYMENT DISCOUNT NOTICE POSTED IN CASH REGISTER AREA

LOOKING TO MAKE A FLYER OR A POSTED NOTICE FOR CUSTOMERS PAYING FOR OVER-THE-COUNTER MERCHANDISE AND WHO PAY BY CASH METHOD TO GET A 4% CASH DISCOUNT.
PRESCRIPTIONS ARE EXCLUDED FROM THIS CASH DISCOUNT.

Target Market(s)

RETAIL CUSTOMERS

Industry/Entity Type

RETAIL PHARMACY

Colors
0054AA
0677BA
7BADD7
CADEEF
E8F1F8
EB3D1F
EC4F4E
F09395
F8D3D4
FCEDEE

Requirements
Must have
• LOGO COLORS
Nice to have
• EYE CATCHING

```html
<!DOCTYPE html>
<html lang="en">
<head>
<meta charset="UTF-8">
<title>Cash Discount Notice – Kellan Bros. Pharmacy</title>
<link href="https://fonts.googleapis.com/css2?family=Open+Sans:wght@700;800&family=Montserrat:wght@900&display=swap" rel="stylesheet">
<style>
  :root {
    --blue-deep: #0054AA;
    --blue-mid: #0677BA;
    --blue-bright: #1E8FE0;
    --blue-soft: #7BADD7;
    --blue-pale: #CADEEF;
    --blue-mist: #E8F1F8;
    --red: #EB3D1F;
    --red-deep: #B3161C;
    --red-rose: #EC4F4E;
    --pink: #F8D3D4;
    --white: #FFFFFF;
    --yellow: #FFE100;
  }
  html, body {
    margin: 0;
    padding: 0;
    width: 1200px;
    height: 1200px;
    overflow: hidden;
    background: var(--white);
  }
  .notice {
    position: relative;
    width: 1200px;
    height: 1200px;
    overflow: hidden;
    font-family: "Open Sans", Arial, sans-serif;
    background: linear-gradient(180deg, #3FA3EE 0%, var(--blue-bright) 45%, #1180D6 100%);
  }
  .notice__texture {
    position: absolute;
    inset: 0;
    background:
      radial-gradient(circle at 18% 30%, rgba(255,255,255,0.12), transparent 35%),
      radial-gradient(circle at 85% 22%, rgba(255,255,255,0.10), transparent 30%),
      radial-gradient(circle at 70% 70%, rgba(0,84,170,0.12), transparent 40%);
  }
  .header-arc {
    position: absolute;
    left: 0;
    top: 0;
  }
  .brand {
    position: absolute;
    top: 78px;
    left: 0;
    width: 1200px;
    display: flex;
    justify-content: center;
    align-items: center;
    gap: 22px;
  }
  .brand__dot {
    width: 56px;
    height: 56px;
    border-radius: 50%;
    background: var(--blue-deep);
  }
  .brand__name {
    font-family: "Open Sans", Arial, sans-serif;
    font-weight: 800;
    font-size: 62px;
    color: var(--red-deep);
    letter-spacing: 0.5px;
  }
  .lead {
    position: absolute;
    top: 318px;
    left: 0;
    width: 1200px;
    margin: 0;
    text-align: center;
    color: var(--white);
    font-weight: 700;
    font-size: 44px;
    line-height: 55px;
    letter-spacing: 0.2px;
  }
  .offer__figure {
    position: absolute;
    left: 178px;
    top: 446px;
    font-family: "Open Sans", Arial, sans-serif;
    font-weight: 800;
    font-size: 440px;
    line-height: 1;
    color: var(--white);
    letter-spacing: -10px;
    text-shadow: -14px 10px 0 var(--blue-deep);
  }
  .offer__percent {
    position: absolute;
    left: 400px;
    top: 473px;
    font-family: "Open Sans", Arial, sans-serif;
    font-weight: 800;
    font-size: 185px;
    line-height: 1;
    color: var(--white);
  }
  .offer__label {
    position: absolute;
    left: 180px;
    top: 865px;
    margin: 0;
    font-family: "Montserrat", Arial, sans-serif;
    font-weight: 900;
    font-size: 83px;
    line-height: 66px;
    color: var(--yellow);
    text-shadow: -5px 4px 0 var(--blue-deep);
  }
  .product-art {
    position: absolute;
    left: 615px;
    top: 505px;
    width: 425px;
    height: 395px;
    border-radius: 40px;
    background: linear-gradient(160deg, var(--blue-mist) 0%, var(--blue-pale) 45%, #2A3440 100%);
    opacity: 0.9;
  }
  .exclusion {
    position: absolute;
    left: 98px;
    top: 1024px;
    width: 1002px;
    height: 86px;
    box-sizing: border-box;
    border: 4px solid var(--white);
    border-radius: 43px;
    background: linear-gradient(180deg, #E8362A 0%, var(--red-deep) 60%, #8E0F13 100%);
    display: flex;
    align-items: center;
    justify-content: center;
    color: var(--white);
    font-weight: 800;
    font-size: 28px;
    letter-spacing: 0.2px;
    box-shadow: 0 4px 10px rgba(0,40,90,0.3);
  }
  .website {
    position: absolute;
    top: 1128px;
    left: 0;
    width: 1200px;
    text-align: center;
    color: var(--white);
    font-weight: 700;
    font-size: 27px;
  }
</style>
</head>
<body>
  <main class="notice">
    <div class="notice__texture"></div>

    <svg class="header-arc" width="1200" height="300" viewBox="0 0 1200 300" aria-hidden="true">
      <ellipse cx="600" cy="20" rx="555" ry="252" fill="#B3161C"/>
      <ellipse cx="600" cy="0" rx="548" ry="250" fill="#FFFFFF"/>
    </svg>

    <div class="brand">
      <span class="brand__dot"></span>
      <span class="brand__name">Kellan Bros. Pharmacy</span>
    </div>

    <p class="lead">FOR CUSTOMERS PAYING<br>FOR OVER-THE-COUNTER MERCHANDISE<br>AND WHO PAY BY CASH METHOD TO GET A</p>

    <div class="product-art" role="img" aria-label="Illustration of a pharmacy shopping bag with medicine bottles, pill packs and boxes resting on a tablet"></div>

    <div class="offer__figure">4</div>
    <div class="offer__percent">%</div>
    <p class="offer__label">CASH<br>DISCOUNT.</p>

    <div class="exclusion">PRESCRIPTIONS ARE EXCLUDED FROM THIS CASH DISCOUNT.</div>

    <div class="website">www.kellanbrospharmacy.example.com</div>
  </main>
</body>
</html>
```